Business Card for New Business

Please design a business card using our logo and font files. This is only one card for one person, as listed in details section.

Industry/Entity Type

Business

Contact Information for Business Card

Carl Voserby

Phone 240.318.6624
Cell 703.581.4096
Email carl@moltravex.com

www.moltravex.com

Address
18250 Brennick Lane #314
Damascus, MD 20715

Font styles to use
Sans Serif

Requirements
Must have
• Information listed in detail section. Must be standard card size.

```html
<!DOCTYPE html>
<html lang="en">
<head>
<meta charset="utf-8">
<title>Moltravex Productions – Business Card</title>
<link rel="stylesheet" href="https://fonts.googleapis.com/css2?family=Open+Sans:wght@300;400&display=swap">
<style>
  :root {
    --backdrop: #ececec;
    --paper: #fbfbfb;
    --brand-orange: #d65422;
    --ink: #3c3c3c;
    --ink-soft: #555555;
    --on-orange: #ffffff;
  }
  * { margin: 0; padding: 0; box-sizing: border-box; }
  html, body {
    width: 1200px;
    height: 900px;
    overflow: hidden;
    background: var(--backdrop);
    font-family: "Open Sans", Arial, sans-serif;
  }
  .canvas {
    width: 1200px;
    height: 900px;
    display: flex;
    align-items: center;
    justify-content: center;
    gap: 60px;
  }
  .card {
    width: 490px;
    height: 280px;
    position: relative;
    box-shadow: 0 2px 10px rgba(0,0,0,0.12);
  }

  /* Front side */
  .card--front { background: var(--paper); color: var(--ink); }
  .holder-name {
    position: absolute;
    left: 32px;
    top: 30px;
    font-size: 19px;
    font-weight: 400;
    color: var(--brand-orange);
    letter-spacing: 0.5px;
  }
  .contact-list {
    position: absolute;
    left: 32px;
    top: 108px;
    list-style: none;
    font-size: 12.5px;
    line-height: 19px;
    color: var(--ink);
  }
  .contact-list li { display: flex; align-items: center; gap: 7px; }
  .contact-icon { width: 10px; height: 10px; flex: none; }
  .brand-lockup {
    position: absolute;
    display: flex;
    align-items: center;
    gap: 8px;
    font-weight: 300;
  }
  .card--front .brand-lockup {
    left: 218px;
    top: 112px;
  }
  .brand-dot { width: 22px; height: 22px; flex: none; }
  .brand-name {
    font-size: 22px;
    color: var(--ink);
    letter-spacing: 0.5px;
    white-space: nowrap;
  }
  .address {
    position: absolute;
    right: 32px;
    bottom: 28px;
    text-align: right;
    font-style: normal;
    font-size: 12.5px;
    line-height: 18px;
    color: var(--ink);
  }
  .address .web { color: var(--brand-orange); }

  /* Back side */
  .card--back {
    background: var(--brand-orange);
    color: var(--on-orange);
  }
  .card--back .brand-lockup {
    left: 50%;
    top: 100px;
    transform: translateX(-50%);
  }
  .card--back .brand-name { color: var(--on-orange); font-size: 26px; }
  .card--back .web {
    position: absolute;
    left: 0;
    right: 0;
    top: 178px;
    text-align: center;
    font-size: 12px;
    letter-spacing: 0.3px;
  }
</style>
</head>
<body>
<main class="canvas">
  <section class="card card--front" aria-label="Business card front">
    <h1 class="holder-name">Carl Voserby</h1>
    <ul class="contact-list">
      <li>
        <svg class="contact-icon" viewBox="0 0 10 10" aria-hidden="true"><path d="M2 1h2l1 2.5-1.3.8a5 5 0 0 0 2 2l.8-1.3L9 6v2a1 1 0 0 1-1 1A7 7 0 0 1 1 2a1 1 0 0 1 1-1z" fill="#d65422"/></svg>
        <span>240.318.6624</span>
      </li>
      <li>
        <svg class="contact-icon" viewBox="0 0 10 10" aria-hidden="true"><rect x="2.5" y="0.5" width="5" height="9" rx="1" fill="#d65422"/><rect x="3.5" y="1.8" width="3" height="5.5" fill="#fbfbfb"/></svg>
        <span>703.581.4096</span>
      </li>
      <li>
        <svg class="contact-icon" viewBox="0 0 10 10" aria-hidden="true"><rect x="0.5" y="2" width="9" height="6.5" fill="#d65422"/><path d="M0.8 2.3 5 5.6 9.2 2.3" fill="none" stroke="#fbfbfb" stroke-width="0.9"/></svg>
        <span>carl@moltravex.com</span>
      </li>
    </ul>
    <div class="brand-lockup">
      <svg class="brand-dot" viewBox="0 0 22 22" aria-hidden="true"><circle cx="11" cy="11" r="10" fill="#d65422"/></svg>
      <span class="brand-name">Moltravex Productions</span>
    </div>
    <address class="address">
      18250 Brennick Lane #314<br>
      Damascus, MD 20715<br>
      <span class="web">www.moltravex.com</span>
    </address>
  </section>

  <section class="card card--back" aria-label="Business card back">
    <div class="brand-lockup">
      <svg class="brand-dot" viewBox="0 0 22 22" aria-hidden="true"><circle cx="11" cy="11" r="10" fill="#ffffff"/></svg>
      <span class="brand-name">Moltravex Productions</span>
    </div>
    <p class="web">www.moltravex.com</p>
  </section>
</main>
</body>
</html>
```